Poem Handwritten by Veteran while in the jungle of Vietnam

My parents are celebrating their 50th wedding anniversary this year. I wanted to give them a very memorable gift. On my parents 2nd anniversary, my father was stationed in Vietnam. On that night he was in the jungle waiting till morning and wrote a poem to my mother using his pant leg as paper. I would like this poem to typographically designed to be framed and hung on the wall.

I have attached a picture of the poem below. It will need to be 11x14 when printed for framing. It would be great if there was background or artwork to make it more visually interesting, perhaps in a watercolor. My parents have a transitional style. I have attached some possible color schemes as well. Cool greens, blue, neutral grays, with hints of berries or highlights of yellow. These are just a guide, I would be open to your interpretations.

Thank you for your help. This will hopefully be a gift they will truly treasure as much as the poem itself.

Target Market(s)

My parents who are excited to be celebrating their 50th wedding anniversary. It should have a transitional, mature style.

Font styles to use
Serif
Script

Requirements
Must have
• The poem, typographically designed. There can be a mix of fonts, but legibility is critically important.
• Now that some designs have come through I wanted to give some more guidance of what I'm looking for. I want something that feels sophisticated and artistic.
Nice to have
• A background or art work, using the color schemes attached as a guide. I am really liking the designs that have a full color landscape artwork in the background. The fonts should be elegant and formal. I really like the romantic, muted colors. I had trouble finding similar projects online in the style I wanted until I cam across wedding invites. Those seem to be the most applicable. I've added pictures of some so you can get a sense of what I'm looking for. I am really liking the jungle foliage, starry skies or sunrises.
Should not have
• Cartoon caricatures, fonts that are too illegible when printed. I'm not liking anything whimsical. I don't like the very bright colors for this project.

```html
<!DOCTYPE html>
<html lang="en">
<head>
<meta charset="utf-8">
<title>Happy Anniversary Darling — Walter's Anniversary Poem</title>
<link rel="stylesheet" href="https://fonts.googleapis.com/css2?family=Great+Vibes&family=Kalam:wght@400&family=Tinos&family=Montserrat:wght@400&display=swap">
<style>
  :root {
    --paper: #ffffff;
    --plum: #6b2a78;
    --ink: #2e2e2e;
    --berry: #a52f5e;
    --berry-dark: #7e1f44;
    --leaf: #3f4d3a;
    --twig: #7a5a4c;
  }
  * { margin: 0; padding: 0; box-sizing: border-box; }
  html, body {
    width: 943px; height: 1200px; overflow: hidden; background: var(--paper);
  }
  .poster {
    position: relative; width: 943px; height: 1200px; background: var(--paper);
  }
  .flourish { position: absolute; left: 0; top: 0; }
  .happy {
    position: absolute; left: 122px; top: 130px;
    font-family: "Montserrat", sans-serif; font-size: 27px; letter-spacing: 3px;
    color: var(--plum); transform: rotate(-33deg); transform-origin: left bottom;
  }
  .anniversary {
    position: absolute; left: 150px; top: 86px; width: 620px;
    font-family: "Great Vibes", cursive; font-size: 132px; line-height: 1;
    color: var(--plum); text-align: center;
  }
  .darling {
    position: absolute; left: 412px; top: 240px;
    font-family: "Great Vibes", cursive; font-size: 56px; line-height: 1;
    color: var(--plum);
  }
  .art { position: absolute; }
  .bouquet-top { left: 303px; top: 307px; width: 322px; height: 90px; }
  .bouquet-bottom { left: 566px; top: 1065px; width: 212px; height: 90px; }
  .bud { width: 42px; height: 46px; }
  .heading {
    position: absolute; left: 0; width: 943px; text-align: center;
    font-family: "Kalam", cursive; color: var(--plum); line-height: 1;
  }
  .heading-date { top: 420px; font-size: 38px; padding-left: 40px; }
  .heading-title { top: 474px; font-size: 38px; }
  .poem {
    position: absolute; top: 569px; width: 380px; text-align: center;
    font-family: "Tinos", serif; font-size: 15.4px; letter-spacing: 1.3px;
    line-height: 19.65px; color: var(--ink);
  }
  .poem-left { left: 85px; }
  .poem-right { left: 478px; }
  .stanza { margin-bottom: 19.65px; }
</style>
</head>
<body>
<main class="poster">
  <svg class="flourish" width="943" height="1200" viewBox="0 0 943 1200" aria-hidden="true">
    <path d="M148 240 C 190 180, 260 190, 320 225 C 360 248, 400 250, 420 245"
          fill="none" stroke="var(--plum)" stroke-width="2"/>
    <path d="M600 265 C 660 275, 720 282, 770 262 C 800 248, 790 230, 760 238 C 720 250, 640 270, 600 265"
          fill="none" stroke="var(--plum)" stroke-width="2"/>
    <circle cx="425" cy="132" r="3.5" fill="var(--plum)"/>
  </svg>

  <div class="happy">HAPPY</div>
  <div class="anniversary">Anniversary</div>
  <div class="darling">Darling</div>

  <svg class="art bouquet-top" viewBox="0 0 322 90" role="img" aria-label="Illustrated bouquet of berry-pink flowers on bare twigs">
    <defs>
      <radialGradient id="bloomTop" cx="50%" cy="50%" r="50%">
        <stop offset="0%" stop-color="#b8457a"/>
        <stop offset="100%" stop-color="#f3d6e1" stop-opacity="0"/>
      </radialGradient>
    </defs>
    <ellipse cx="161" cy="45" rx="160" ry="44" fill="url(#bloomTop)"/>
  </svg>

  <svg class="art bud" style="left:120px;top:60px" viewBox="0 0 42 46" role="img" aria-label="Berry flower bud"><ellipse cx="21" cy="23" rx="19" ry="21" fill="var(--berry)"/></svg>
  <svg class="art bud" style="left:776px;top:100px" viewBox="0 0 42 46" role="img" aria-label="Berry flower bud"><ellipse cx="21" cy="23" rx="19" ry="21" fill="var(--berry)"/></svg>
  <svg class="art bud" style="left:100px;top:380px" viewBox="0 0 42 46" role="img" aria-label="Berry flower bud"><ellipse cx="21" cy="23" rx="16" ry="20" fill="var(--berry)"/></svg>
  <svg class="art bud" style="left:778px;top:480px" viewBox="0 0 42 46" role="img" aria-label="Berry flower bud"><ellipse cx="21" cy="23" rx="17" ry="19" fill="var(--berry)"/></svg>
  <svg class="art bud" style="left:472px;top:990px" viewBox="0 0 42 46" role="img" aria-label="Berry flower bud"><ellipse cx="21" cy="23" rx="15" ry="17" fill="var(--berry-dark)"/></svg>
  <svg class="art bud" style="left:70px;top:1085px" viewBox="0 0 42 46" role="img" aria-label="Berry flower bud"><ellipse cx="21" cy="21" rx="20" ry="17" fill="var(--berry-dark)"/></svg>

  <h1 class="heading heading-date">20 July 1970, Monday, LZ Sentinel</h1>
  <h2 class="heading heading-title">Walter's Anniversary Poem</h2>

  <section class="poem poem-left">
    <p class="stanza">Life's journey began with a challenge,<br>It was heralded far and near.<br>The road led on forever,<br>Its completion was known to be dear.</p>
    <p class="stanza">From the garden of light it proceeded,<br>To the valley of shadows it led.<br>Thorns and thistles adorned it,<br>Past abyss and crevice it sped.</p>
    <p class="stanza">The brave surged forward with courage,<br>The wise undaunted pressed on.<br>The mighty held high their banner,<br>We all awaited the dawn.</p>
    <p class="stanza">Though the pitfalls and hazards were many,<br>The pathway was clearly in view.<br>Straight and sure it glided,<br>Its course we knew to be true.</p>
    <p class="stanza">I knew you, Sweetheart, beforehand,<br>So precious and sweet were you.<br>Our moments of bliss were priceless,<br>Each day brought us joy anew.</p>
    <p class="stanza">The call to progression beckoned,<br>At last I would have my chance—<br>To clasp you to me forever,<br>And seal our divine romance.</p>
  </section>

  <section class="poem poem-right">
    <p class="stanza">I eagerly started the journey,<br>Though with sorrow, I left you behind.<br>With courage and faith I continued,<br>For I knew, that you later I'd find.</p>
    <p class="stanza">I diligently searched for you. Darling.<br>The roadway was both bleak and fair.<br>Though the years grew long in number,<br>I did not give up in despair.</p>
    <p class="stanza">At last in the distance I saw you.<br>So beautiful, lovely, and sweet!<br>Your attention I struggled to capture,<br>Your love I wrested to meet.</p>
    <p class="stanza">What rapture was mine in fulfillment,<br>As now together we stand.<br>To cherish and love each other.<br>While our plans and dreams expand.</p>
    <p class="stanza">I love you, Darling, forever,<br>My life you have made replete.<br>Our eternal mansion beckons,<br>Your love has made it complete.</p>
  </section>

  <svg class="art bouquet-bottom" viewBox="0 0 212 90" role="img" aria-label="Illustrated spray of berry-pink flowers with dark green leaves">
    <defs>
      <radialGradient id="bloomBottom" cx="50%" cy="50%" r="50%">
        <stop offset="0%" stop-color="#b8457a"/>
        <stop offset="70%" stop-color="#8a9a86" stop-opacity="0.5"/>
        <stop offset="100%" stop-color="#ffffff" stop-opacity="0"/>
      </radialGradient>
    </defs>
    <ellipse cx="106" cy="45" rx="105" ry="44" fill="url(#bloomBottom)"/>
  </svg>
</main>
</body>
</html>
```